Business Card Design for Flood Rescue 360 - Property Restoration Professionals

I need a business card designed for Flood Rescue 360. We are a full-service property restoration solution. Providing water, fire, smoke & storm restoration as well as mold remediation and full remodel or reconstruction to homes and businesses across Dallas-Fort Worth, TX.
Target Market(s)
home and business owners with insurance covered property damage from water, fire or storm related damage
Industry/Entity Type
property restoration
Contact Information for Business Card
Martin Kell General Manager Cell: 214-555-0193 Office: 469-555-0148 email: Martin@FloodRescue360.example services: Water, Fire, Mold, Reconstruction Tagline: Rapid Response When Floods Strike!
Look and feel
Each slider illustrates characteristics of the customer's brand and the style your logo design should communicate.

```html
<!DOCTYPE html>
<html lang="en">
<head>
<meta charset="utf-8">
<title>Flood Rescue 360 — Business Card</title>
<link rel="stylesheet" href="https://fonts.googleapis.com/css2?family=Montserrat:wght@400;600;700&family=Roboto+Condensed:wght@900&display=swap">
<style>
  :root {
    --brand-blue: #14b4e6;
    --faint-blue: #dff3fa;
    --ink: #2b2b2b;
    --paper: #ffffff;
    --backdrop: #3a3a3c;
  }
  * { margin: 0; padding: 0; box-sizing: border-box; }
  html, body {
    width: 1200px; height: 1059px; overflow: hidden;
    background: var(--backdrop);
  }
  .canvas { position: relative; width: 1200px; height: 1059px; }
  .card {
    position: absolute; border-radius: 22px; overflow: hidden;
    box-shadow: 0 14px 26px rgba(0,0,0,.55);
  }
  .card-front { left: 256px; top: 100px; width: 688px; height: 391px; background: var(--paper); }
  .card-back { left: 253px; top: 537px; width: 694px; height: 394px; background: var(--brand-blue); }

  .wordmark {
    font-family: "Roboto Condensed", "Arial Narrow", sans-serif;
    font-weight: 900; line-height: .86; letter-spacing: -.5px;
    text-transform: uppercase; white-space: nowrap;
  }
  .front-wordmark { position: absolute; left: 30px; top: 34px; display: flex; align-items: center; gap: 12px; }
  .front-wordmark .wordmark { font-size: 50px; color: var(--brand-blue); }
  .mark-dot { border-radius: 50%; flex: none; }
  .front-wordmark .mark-dot { width: 78px; height: 78px; background: var(--brand-blue); }

  .faint-emblem {
    position: absolute; left: 345px; top: 35px; width: 322px; height: 322px;
    border-radius: 50%; background: var(--faint-blue);
  }

  .person { position: absolute; left: 29px; top: 150px; font-family: "Montserrat", sans-serif; }
  .person-name { font-size: 33px; font-weight: 700; color: var(--brand-blue); letter-spacing: 1px; line-height: 1.1; white-space: nowrap; }
  .person-role { font-size: 16px; font-weight: 400; color: var(--ink); margin-top: 0; letter-spacing: .3px; }
  .rule { width: 21px; height: 2px; background: var(--brand-blue); }
  .rule-top { position: absolute; left: 29px; top: 213px; }
  .rule-bottom { position: absolute; left: 29px; top: 334px; }

  .contact-list { position: absolute; left: 29px; top: 226px; list-style: none; font-family: "Montserrat", sans-serif; }
  .contact-list li { display: flex; align-items: center; gap: 9px; height: 24.7px; font-size: 17px; color: var(--ink); letter-spacing: .3px; white-space: nowrap; }
  .contact-list svg { width: 12px; height: 12px; fill: var(--brand-blue); flex: none; }

  .tagline { position: absolute; left: 29px; top: 345px; font-family: "Montserrat", sans-serif; font-size: 16px; color: var(--ink); letter-spacing: .4px; white-space: nowrap; }

  .back-wordmark { position: absolute; left: 0; right: 0; top: 132px; display: flex; justify-content: center; align-items: center; gap: 14px; }
  .back-wordmark .wordmark { font-size: 68px; color: var(--paper); }
  .back-wordmark .mark-dot { width: 128px; height: 128px; background: var(--paper); }

  .services { position: absolute; left: 0; right: 0; top: 334px; display: flex; justify-content: center; gap: 20px; list-style: none; font-family: "Montserrat", sans-serif; font-size: 17px; color: var(--paper); letter-spacing: .5px; }
  .services li { display: flex; align-items: center; gap: 11px; }
  .services svg { width: 11px; height: 15px; fill: var(--paper); }
</style>
</head>
<body>
<main class="canvas">
  <section class="card card-front">
    <div class="faint-emblem" aria-hidden="true"></div>
    <div class="front-wordmark">
      <div class="wordmark">Flood<br>Rescue 360</div>
      <span class="mark-dot" aria-hidden="true"></span>
    </div>
    <div class="person">
      <h1 class="person-name">MARTIN KELL</h1>
      <p class="person-role">General Manager</p>
    </div>
    <div class="rule rule-top"></div>
    <ul class="contact-list">
      <li><svg viewBox="0 0 24 24"><path d="M6.6 10.8a15 15 0 0 0 6.6 6.6l2.2-2.2c.3-.3.7-.4 1-.2 1.1.4 2.3.6 3.6.6.6 0 1 .4 1 1V20c0 .6-.4 1-1 1A17 17 0 0 1 3 4c0-.6.4-1 1-1h3.5c.6 0 1 .4 1 1 0 1.3.2 2.5.6 3.6.1.3 0 .7-.2 1z"/></svg>214-555-0193</li>
      <li><svg viewBox="0 0 24 24"><path d="M7 1h10a2 2 0 0 1 2 2v18a2 2 0 0 1-2 2H7a2 2 0 0 1-2-2V3a2 2 0 0 1 2-2zm0 3v14h10V4zm5 15.5a1 1 0 1 0 0 2 1 1 0 0 0 0-2z"/></svg>469-555-0148</li>
      <li><svg viewBox="0 0 24 24"><path d="M2 5h20v14H2zm2 2v.5l8 5 8-5V7z"/></svg>Martin@FloodRescue360.example</li>
      <li><svg viewBox="0 0 24 24"><path d="M12 2a10 10 0 1 0 0 20 10 10 0 0 0 0-20zm6.9 6h-3a15 15 0 0 0-1.3-3.9A8 8 0 0 1 18.9 8zM12 4c.8 1.2 1.5 2.5 1.9 4h-3.8c.4-1.5 1.1-2.8 1.9-4zM4.3 14a8 8 0 0 1 0-4h3.4a16 16 0 0 0 0 4zm.8 2h3a15 15 0 0 0 1.3 3.9A8 8 0 0 1 5.1 16zm3-8h-3a8 8 0 0 1 4.3-3.9A15 15 0 0 0 8.1 8zM12 20c-.8-1.2-1.5-2.5-1.9-4h3.8c-.4 1.5-1.1 2.8-1.9 4zm2.3-6H9.7a14 14 0 0 1 0-4h4.6a14 14 0 0 1 0 4zm.3 5.9a15 15 0 0 0 1.3-3.9h3a8 8 0 0 1-4.3 3.9zm1.7-5.9a16 16 0 0 0 0-4h3.4a8 8 0 0 1 0 4z"/></svg>www.FloodRescue360.example</li>
    </ul>
    <div class="rule rule-bottom"></div>
    <p class="tagline">Rapid Response When Floods Strike!</p>
  </section>

  <section class="card card-back">
    <div class="back-wordmark">
      <div class="wordmark">Flood<br>Rescue 360</div>
      <span class="mark-dot" aria-hidden="true"></span>
    </div>
    <ul class="services">
      <li><svg viewBox="0 0 11 15"><path d="M5.5 0C4 3 0 6.5 0 9.5a5.5 5.5 0 0 0 11 0C11 6.5 7 3 5.5 0z"/></svg>Water</li>
      <li><svg viewBox="0 0 11 15"><path d="M5.5 0C4 3 0 6.5 0 9.5a5.5 5.5 0 0 0 11 0C11 6.5 7 3 5.5 0z"/></svg>Fire</li>
      <li><svg viewBox="0 0 11 15"><path d="M5.5 0C4 3 0 6.5 0 9.5a5.5 5.5 0 0 0 11 0C11 6.5 7 3 5.5 0z"/></svg>Mold</li>
      <li><svg viewBox="0 0 11 15"><path d="M5.5 0C4 3 0 6.5 0 9.5a5.5 5.5 0 0 0 11 0C11 6.5 7 3 5.5 0z"/></svg>Reconstruction</li>
    </ul>
  </section>
</main>
</body>
</html>
```